Website Design for Business Law Firm

We have a logo and now we would like a web site design for our new website. Our small firm provides creative and aggressive transactional (not litigation) legal services to advise healthcare, technology, internet-based and traditional companies and investors in such companies on healthcare, technology, financing, mergers/acquisitions, real estate and other transactions, legal compliance and general corporate and business matters.

We would like to see a website design that is professional and appropriate for executives, professionals, investors and government regulators to visit, that conveys professionalism and competence while being a little edgy and modern - no typical legal motifs such as gavels, books, or scales of justice. We advise businesses and investors and guide them through complicated issues quickly, capably and differently from other law firms. We are part of the business team and get things done.

The logo is attached, and we like gray as a color to complement it. The intention of the logo is to convey that in a storm or challenging time, people come to this firm, and people come to this firm when they need the power and disruption to change things or shake them up.

I have also enclosed a picture of our business card for consideration.

On the other hand, you can check out the current simple site at www.venhollow.example to see we have used a space motif in the past to evoke that we help create stars (the nebula featured there). This is not a necessary part of the new website and it may look better without it.

We appreciate your creativity and look forward to designs.

Industry/Entity Type

Business

Requirements
Must have
• We anticipate the following pages, and you may submit different ideas for the different pages:
• 1. Landing page
• 2. Services pages - healthcare, IT/Technology, general counsel services, financings, mergers/acquisitions, mediation/arbitration, procurement and productization
• 3. About Us including contact information
• Our name and contact information:
• Quellane Law Firm, P.C.
• 8716 SW 19th Ave.
• Portland, OR 97213
• phone: 971.555.0143
• fax: 971.555.0187
Nice to have
• Please consider designs that enhance the impressions we are looking for
Should not have
• Please no gavels, scales of justice, law books, or similar traditional legal imagery.

```html
<!DOCTYPE html>
<html lang="en">
<head>
<meta charset="utf-8">
<title>Quellane Law Firm</title>
<link rel="stylesheet" href="https://fonts.googleapis.com/css2?family=Open+Sans:wght@300;400;600&family=Noto+Serif:wght@400&display=swap">
<style>
:root{
  --page-bg:#f1efe6;
  --stripe:#e6e3d6;
  --panel:#ffffff;
  --ink:#555555;
  --ink-soft:#8a8a8a;
  --ink-dark:#333333;
  --nav-active:#8c8c8c;
  --rule:#9a9a9a;
}
*{box-sizing:border-box;margin:0;padding:0}
html,body{width:1200px;height:1158px;overflow:hidden}
body{
  position:relative;
  font-family:"Open Sans",Arial,sans-serif;
  color:var(--ink);
  background:repeating-linear-gradient(90deg,var(--page-bg) 0 6px,var(--stripe) 6px 9px);
}
.sheet{
  position:absolute;left:97px;top:0;width:1021px;height:1087px;
  background:var(--panel);box-shadow:0 2px 8px rgba(0,0,0,.25);
}
.brand{
  position:absolute;left:110px;top:32px;width:342px;height:83px;
  display:flex;align-items:center;gap:14px;
  font-family:"Open Sans",sans-serif;font-weight:300;font-size:44px;letter-spacing:6px;color:var(--ink-dark);
}
.brand-mark{width:22px;height:22px;background:var(--ink-dark);flex:none}
.main-nav{position:absolute;left:497px;top:56px;display:flex;font-size:13px;color:var(--ink-dark)}
.main-nav a{color:inherit;text-decoration:none;padding:6px 10px;height:29px;line-height:17px;margin-right:10px}
.main-nav a.active{background:var(--nav-active);color:#fff;border-radius:2px}
.nav-rule{position:absolute;left:495px;top:112px;width:595px;height:4px;border-top:1px solid var(--rule);border-bottom:1px solid var(--rule)}
.hero{
  position:absolute;left:109px;top:141px;width:982px;height:301px;border:1px solid #cfcfcf;overflow:hidden;
  background:linear-gradient(90deg,#f7f7f5 0%,#f2f1ec 40%,#e9e6df 100%);
}
.hero-photo{position:absolute;left:370px;top:0;width:612px;height:300px;
  background:linear-gradient(90deg,rgba(242,241,236,0) 0%,#c9c4bc 30%,#a39c93 60%,#5a5550 100%)}
.hero-title{position:absolute;left:24px;top:82px;font-family:"Noto Serif",serif;font-size:24px;line-height:30px;color:#666;font-weight:400;width:300px}
.hero-phone{position:absolute;left:27px;top:148px;font-family:"Noto Serif",serif;font-size:31px;color:var(--ink-dark);letter-spacing:1px}
.hero-button{
  position:absolute;left:16px;top:209px;width:271px;height:36px;border-radius:18px;
  background:linear-gradient(#f2f2f2,#c9c9c9);box-shadow:0 1px 3px rgba(0,0,0,.3);
  font-size:14px;color:#444;line-height:36px;padding-left:19px;
}
.hero-button svg{position:absolute;right:11px;top:7px}
.intro{position:absolute;left:118px;top:476px;width:612px}
.intro h2,.locations h2{font-weight:400;font-size:19px;color:#444;letter-spacing:-.3px}
.intro p{font-size:12.6px;line-height:18px;color:var(--ink-soft);margin-top:13px;letter-spacing:.15px}
.intro p + p{margin-top:42px}
.divider{position:absolute;left:757px;top:472px;height:314px;border-left:3px dotted #b5b5b5}
.locations{position:absolute;left:775px;top:474px;width:310px}
.locations h2{font-weight:300;font-size:19px}
.loc{position:absolute;left:0;display:flex;gap:8px}
.loc-thumb{width:94px;height:64px;flex:none}
.loc h3{font-size:12px;font-weight:600;color:#777;margin-top:-2px}
.loc p{font-size:11px;line-height:14px;color:#888;margin-top:6px;padding-left:1px;width:200px}
.callout{position:absolute;left:0;width:1200px;top:849px;text-align:center;font-family:"Noto Serif",serif;font-size:15px;color:#777;letter-spacing:.55px}
.issue{position:absolute;top:890px;width:294px;height:161px}
.issue-photo{position:absolute;inset:0}
.issue h3{position:absolute;left:0;top:0;width:100%;height:28px;background:rgba(30,30,30,.9);color:#fff;text-align:center;font-family:"Noto Serif",serif;font-weight:400;font-size:18px;line-height:28px;letter-spacing:.3px}
.footer{position:absolute;left:0;width:1200px;top:1110px;text-align:center;font-size:12px;color:var(--ink-dark)}
</style>
</head>
<body>
<div class="sheet"></div>

<header>
  <div class="brand"><span class="brand-mark"></span>QUELLANE</div>
  <nav class="main-nav">
    <a class="active" href="#">HOME</a>
    <a href="#">Firm Profile</a>
    <a href="#">Practice Areas</a>
    <a href="#">Recent Deals</a>
    <a href="#">Insights</a>
    <a href="#">Contact Us</a>
  </nav>
  <div class="nav-rule"></div>
</header>

<section class="hero">
  <div class="hero-photo" role="img" aria-label="Photo of business clients meeting with an advisor"></div>
  <h1 class="hero-title">Call us today for a &nbsp;Legal Consultation</h1>
  <div class="hero-phone">971.555.0143</div>
  <div class="hero-button">Learn more about the Quellane
    <svg width="22" height="22" viewBox="0 0 22 22"><circle cx="11" cy="11" r="11" fill="#222"/><path d="M5 11h9M10 6l5 5-5 5" stroke="#fff" stroke-width="2.4" fill="none"/></svg>
  </div>
</section>

<section class="intro">
  <h2>Putting our Knowledge to work for you</h2>
  <p>It is a long established fact that a reader will be distracted by the readable content of a page when looking at its layout. The point of using Lorem Ipsum is that it has a more-or-less normal distribution of letters, as opposed to using 'Content here, content here', making it look like read-able English. Many desktop publishing packages and web page editors now use Lorem Ipsum as their default model text, and a search for 'lorem ipsum' will uncover many web sites still in their infancy. Various versions have evolved over the years, sometimes by accident, sometimes on purpose (injected humour and the like).</p>
  <p>It is a long established fact that a reader will be distracted by the readable content of a page when looking at its layout. The point of using Lorem Ipsum is that it has a more-or-less normal distribution of letters, as opposed to using 'Content here, content here', making it look like read-able English. Many desktop publishing packages and web page editors now use Lorem Ipsum as their default model text, and a search for 'lorem ipsum'</p>
</section>

<div class="divider"></div>

<aside class="locations">
  <h2>Three Convenient locations</h2>
  <div class="loc" style="top:51px">
    <div class="loc-thumb" role="img" aria-label="Photo of a street-front office with palm trees" style="background:linear-gradient(#6d8fa8,#b09a6a 55%,#4d4a3c)"></div>
    <div><h3>The Lorem Lipsum</h3><p>It is a long established fact that a reader will be distracted by the read-</p></div>
  </div>
  <div class="loc" style="top:144px">
    <div class="loc-thumb" role="img" aria-label="Photo of a brick office building" style="background:linear-gradient(#c9cfd4,#8a5a48 45%,#6f7a50)"></div>
    <div><h3>The Lorem Lipsum</h3><p>It is a long established fact that a reader will be distracted by the read-</p></div>
  </div>
  <div class="loc" style="top:247px">
    <div class="loc-thumb" role="img" aria-label="Photo of a large stone building" style="background:linear-gradient(#8fa2b8,#857a68 45%,#5c554a)"></div>
    <div><h3>The Lorem Lipsum</h3><p>It is a long established fact that a reader will be distracted by the read-</p></div>
  </div>
</aside>

<p class="callout">CLICK BELOW TO FIND OUT WHAT YOU SHOULD KNOW ABOUT ISSUES THAT IMPACT YOUR BUSINESS</p>

<article class="issue" style="left:113px">
  <div class="issue-photo" role="img" aria-label="Photo of a row of commercial brick buildings" style="background:linear-gradient(90deg,#8a4a3e,#a5a6ab 50%,#7d7560)"></div>
  <h3>Healthcare Compliance</h3>
</article>
<article class="issue" style="left:457px">
  <div class="issue-photo" role="img" aria-label="Photo of an executive working at an office desk" style="background:linear-gradient(90deg,#3b3028,#a98a62 50%,#6b5236)"></div>
  <h3>Mergers &amp; Acquisitions</h3>
</article>
<article class="issue" style="left:797px">
  <div class="issue-photo" role="img" aria-label="Photo of a columned financial building facade" style="background:linear-gradient(#e6e6e4,#b8b6b0 60%,#8e8b85)"></div>
  <h3>Technology Financing</h3>
</article>

<footer class="footer">Copyrights © 2013 Quellane.example - All Rights Reserved. | Sitemap | Disclaimer</footer>
</body>
</html>
```